Tri-Fold Flyer for Life Coaching Business

We require a tri-fold DL flyer for our Life Coaching business, Tall Harbor.
The flyer needs to be bold, engaging and professional with broad appeal. Ideally it will include a few images and/or graphics, but shouldn’t be too busy.
As a generalist life coaching business, image selection needs to be broad enough to attract clients who are interested in Career, Relationship or General Life Coaching (think Health, Wealth & Balance). Please feel free to use any images/graphics you think are suitable. We have also purchased a selection of images from PixVault that you may wish to use - these can be viewed on our website www.tallharbor-example.com - originals can be requested.
Unlike a lot of coaching businesses, we are not interested in being too cheesy, flowery or spiritual. Our style is direct, up-front and to the point - we don’t take ourselves too seriously. The flyer should reflect this.
Attached is a basic template that shows the required text and an example of layout - however we are very flexible with the layout/design, so please don’t be limited by this (eg. Image on the front is only used as a placeholder, testimonials may work better somewhere else etc).
Also attached is a copy of our business card and logo. This will give you an idea of the designs that we are already using. Again, this is as a guide only - however we would definitely like to use similar fonts to the business card (Helvetica or Helvetica Neue I think) and have the blue from the logo incorporated. It would be great to see icons (similar to what has been used on the business card) for phone number, email address etc. Different versions of the logo (format, colour etc) are available.
Aside from this we would like you to use your creative flair and show us different versions of the flyer. Thank You and Good Luck!
Updates
Hi everyone,
Industry/Entity Type
Life Coaching
Requirements
Must have
- Brochure should be tri-fold DL
Logo should be included - preferably on back cover
Contact details and call to action should be prominent/obvious

```html
<!DOCTYPE html>
<html lang="en">
<head>
<meta charset="utf-8">
<title>Tall Harbor – Tri-Fold Flyer</title>
<link href="https://fonts.googleapis.com/css2?family=Arimo:wght@400;700&display=swap" rel="stylesheet">
<style>
  :root{
    --brand-blue:#1a73c4;
    --deep-blue:#0b4f9c;
    --navy:#0a3c78;
    --sky:#5fb2ec;
    --ink:#333f4b;
    --white:#ffffff;
  }
  *{box-sizing:border-box;margin:0;padding:0}
  html,body{width:898px;height:1200px;overflow:hidden;background:var(--white)}
  body{font-family:"Arimo",Arial,sans-serif;color:var(--ink);position:relative}
  .spread{position:absolute;left:0;width:898px;display:flex}
  .spread--outside{top:0;height:594px}
  .spread--inside{top:612px;height:588px}
  .panel{position:relative;height:100%;overflow:hidden}
  .panel--w1{width:299px}.panel--w2{width:300px}

  /* outside left */
  .questions{position:absolute;left:8px;top:8px;width:283px;height:282px}
  .questions svg{position:absolute;inset:0}
  .questions__text{position:relative;padding:18px 22px 0 22px;color:var(--white);font-weight:700;font-size:16px;line-height:1.3;text-align:center}
  .questions__text p{margin-bottom:18px}
  .questions__text p:nth-child(2){color:#bfe1ff}
  .photo{position:absolute}
  .photo--desk{left:0;top:300px;width:299px;height:294px;background:linear-gradient(180deg,#f2f6f9 0%,#d9e1e8 55%,#b9a48c 100%)}

  /* brand name */
  .brand{font-weight:700;font-size:26px;color:var(--brand-blue);text-align:center}
  .brand--light{color:var(--white)}

  /* outside middle */
  .panel--intro{background:var(--white);padding:24px 26px 0}
  .panel--intro .brand{margin-bottom:24px}
  .body-copy{font-size:10px;line-height:1.45;margin-bottom:10px}
  .contact{position:absolute;left:26px;bottom:60px;right:20px}
  .contact__lead{font-size:10px;line-height:1.45;margin-bottom:8px}
  .contact__row{display:flex;align-items:center;gap:6px;font-size:12px;font-weight:700;color:var(--navy);margin-bottom:5px}
  .contact__row svg{width:13px;height:13px;flex:none}
  .panel--intro::after{content:"";position:absolute;left:0;right:0;bottom:0;height:34px;background:var(--brand-blue)}

  /* outside right */
  .panel--cover{background:linear-gradient(180deg,var(--brand-blue) 0%,var(--deep-blue) 100%);color:var(--white)}
  .panel--cover .brand{position:absolute;top:22px;left:0;right:0}
  .photo--summit{left:0;top:78px;width:299px;height:240px;background:linear-gradient(180deg,#3d8fd6 0%,#8cc6f0 55%,#1f5d9e 100%)}
  .cover-title{position:absolute;right:22px;top:352px;text-align:right;font-weight:700;font-size:20px;line-height:1.2}
  .cover-sub{position:absolute;right:22px;top:418px;text-align:right;font-weight:700;font-size:13px}
  .cover-call{position:absolute;right:22px;top:488px;text-align:right;font-weight:700}
  .cover-call span{display:block;font-size:15px}
  .cover-call strong{display:block;font-size:26px;margin-top:4px}

  /* inside */
  .panel--blue{background:linear-gradient(180deg,var(--brand-blue) 0%,var(--deep-blue) 100%)}
  .panel--light{background:var(--white)}
  .photo--victory{left:0;top:0;width:599px;height:222px;z-index:2;background:linear-gradient(180deg,#2f7fd0 0%,#7ab9ea 60%,#dfeefa 100%)}
  .inside-copy{position:absolute;color:var(--white);font-size:10px;line-height:1.45}
  .inside-copy h2{font-size:16px;font-weight:700;margin-bottom:8px}
  .inside-copy p{margin-bottom:8px}
  .inside-copy ul{list-style:none;padding-left:10px;margin-bottom:8px}
  .inside-copy li::before{content:"– "}
  .copy--about{left:18px;top:238px;width:265px}
  .copy--who{left:18px;top:238px;width:264px}
  .copy--how{left:18px;top:22px;width:262px;color:var(--ink)}
  .copy--how h2{color:var(--deep-blue)}
  .quote{font-style:italic;background:var(--brand-blue);color:var(--white);padding:8px;border-radius:4px}
</style>
</head>
<body>

<section class="spread spread--outside">
  <div class="panel panel--w1">
    <div class="questions">
      <svg viewBox="0 0 283 282" preserveAspectRatio="none" aria-hidden="true">
        <path d="M10 0H273a10 10 0 0 1 10 10V250a10 10 0 0 1-10 10H70l-24 22v-22H10a10 10 0 0 1-10-10V10A10 10 0 0 1 10 0Z" fill="#0b4f9c"/>
      </svg>
      <div class="questions__text">
        <p>Are you stuck in a rut or at a crossroads in life?</p>
        <p>Do you have ongoing problems with your career, relationship or just life itself?</p>
        <p>Would you like to change your direction, or regain some clarity to life?</p>
      </div>
    </div>
    <div class="photo photo--desk" role="img" aria-label="Photo of a thoughtful woman resting her chin on her hand at a desk"></div>
  </div>

  <div class="panel panel--w2 panel--intro">
    <div class="brand">Tall Harbor</div>
    <p class="body-copy">Tall Harbor is a professional coaching service that helps people like you achieve the outcomes that you're looking for. It doesn't matter what the challenge is, coaching can take you from where you are now, to where you want to be.</p>
    <p class="body-copy">If you are ready to take your life to the next level and would like to know more, please get in touch. Our introductory sessions are complimentary and totally obligation free, so why not give it a go? We look forward to hearing from you.</p>
    <div class="contact">
      <p class="contact__lead">Call now for a free introductory session or visit our website to download our e-book:</p>
      <div class="contact__row"><svg viewBox="0 0 16 16" aria-hidden="true"><path d="M3 1h3l1.5 4-2 1.2a9 9 0 0 0 4.3 4.3L11 8.5l4 1.5v3a2 2 0 0 1-2 2A12 12 0 0 1 1 3a2 2 0 0 1 2-2Z" fill="#1a73c4"/></svg>(03) 5550 1827</div>
      <div class="contact__row"><svg viewBox="0 0 16 16" aria-hidden="true"><rect x="1" y="3" width="14" height="10" rx="1.5" fill="#1a73c4"/><path d="M1.5 4 8 9l6.5-5" stroke="#fff" fill="none" stroke-width="1.3"/></svg>info@tallharbor-example.com</div>
      <div class="contact__row"><svg viewBox="0 0 16 16" aria-hidden="true"><circle cx="8" cy="8" r="7" fill="#1a73c4"/><path d="M1 8h14M8 1c-3 3.5-3 10.5 0 14M8 1c3 3.5 3 10.5 0 14" stroke="#fff" fill="none" stroke-width="1"/></svg>www.tallharbor-example.com</div>
    </div>
  </div>

  <div class="panel panel--w1 panel--cover">
    <div class="brand brand--light">Tall Harbor</div>
    <div class="photo photo--summit" role="img" aria-label="Photo of a person standing on a mountain summit against a blue sky"></div>
    <p class="cover-title">TAKE CONTROL<br>of your life right now!</p>
    <p class="cover-sub">Career, Relationship &amp; Life Coaching</p>
    <p class="cover-call"><span>CALL NOW!</span><strong>(03) 5550 1827</strong></p>
  </div>
</section>

<section class="spread spread--inside">
  <div class="photo photo--victory" role="img" aria-label="Photo of a businessman raising his arms in celebration under a bright sky"></div>
  <div class="panel panel--w1 panel--blue">
    <div class="inside-copy copy--about">
      <h2>What is coaching all about?</h2>
      <p>Life coaching is one of the fastest growing professions and helps people take real steps towards the life they want. It is not therapy and it is not advice; it is a focused partnership built around your goals.</p>
      <p>We use proven processes that help you find clarity, set priorities and build momentum. Your coach keeps you accountable so that change actually happens.</p>
      <p>Think of coaching as a conversation that moves you forward, one clear step at a time, with someone firmly in your corner.</p>
    </div>
  </div>

  <div class="panel panel--w2 panel--blue">
    <div class="inside-copy copy--who">
      <h2>Who is it for?</h2>
      <p>It's for anyone who wants more from life and is willing to do something about it. Our clients come from all walks of life, careers and stages.</p>
      <p>Coaching is a practical way of dealing with:</p>
      <ul>
        <li>Career change and direction</li>
        <li>Relationship challenges</li>
        <li>Health, wealth and balance</li>
        <li>Confidence and motivation</li>
        <li>Setting and reaching goals</li>
      </ul>
    </div>
  </div>

  <div class="panel panel--w1 panel--light">
    <div class="inside-copy copy--how">
      <h2>How does it work?</h2>
      <p>Sessions run by phone or in person, at a time that suits you. We start by working out where you are now and where you want to be, then build a plan to get there.</p>
      <h2>What will you get out of it?</h2>
      <p>Clarity, focus and real results. You will finish with a clear plan, new habits and the confidence to keep moving forward on your own.</p>
      <p class="quote">"Straight talking and practical. Within weeks I had a plan and the drive to follow it through."</p>
      <p class="quote">"I finally made the career move I had put off for years. Highly recommended."</p>
    </div>
  </div>
</section>

</body>
</html>
```